Marrowind Vodka logo and label design

We would like a logo and bottle label design for a new line of Ultra-Premium Vodka. The Company is called Marrowind Spirits and is based in Brisbane, Australia. We would like a 'Gatsby/Prohibition era vibe to the design. We want to keep it minimalistic and sleek. We strongly prefer a minimalist design and colour palette. Black,Gold,Grey,White,Silver,Red and Blue

The bottle will be similar in shape to Calloway/Pale Heron. There will also need to be space on the label for required information, as well as short bio of the company, which will be provided to the winning design.

We would like to add the polish code of arms for Opoczno. Have attached link for reference. https://www.crestarchive-example.org/crestarchive/index.php?title=Opoczno

Target Market(s)

Luxury brand customers

Logo Text

Marrowind Ultra-Premium Vodka

Logo styles of interest
Wordmark Logo
Lettermark Logo
Requirements
Must have
• This is the first release from our new Vodka label. We want a logo and bottle label that reflects a premium product. We very much like Prohibition/Gatsby era themed bottles and labels. The label and bottle should be elegant and clean.
Should not have
• Anything too busy or confusing.

```html
<!DOCTYPE html>
<html lang="en">
<head>
<meta charset="utf-8">
<title>Marrowind Ultra-Premium Vodka – Label</title>
<link rel="stylesheet" href="https://fonts.googleapis.com/css2?family=Federo&family=Cormorant+Garamond:wght@500&display=swap">
<style>
  :root {
    --paper: #ffffff;
    --navy: #02002b;
    --gold: #d59a5a;
  }
  html, body {
    margin: 0;
    padding: 0;
    width: 1200px;
    height: 928px;
    overflow: hidden;
    background: var(--paper);
  }
  .label-canvas {
    display: block;
    width: 1200px;
    height: 928px;
  }
  .label-ground { fill: var(--navy); stroke: var(--gold); stroke-width: 1; }
  .frame-outer { fill: none; stroke: var(--gold); stroke-width: 5; }
  .frame-inner { fill: none; stroke: var(--gold); stroke-width: 1.6; }
  .crest-shield { fill: var(--gold); }
  .brand-name {
    font-family: "Federo", sans-serif;
    font-size: 62px;
    fill: var(--gold);
  }
  .product-line {
    font-family: "Federo", sans-serif;
    font-size: 30px;
    font-variant: small-caps;
    fill: var(--gold);
  }
  .divider-dots {
    stroke: var(--gold);
    stroke-width: 2.5;
    stroke-dasharray: 1.5 2;
  }
  .origin-line {
    font-family: "Cormorant Garamond", serif;
    font-weight: 500;
    font-size: 19px;
    letter-spacing: 0.5px;
    fill: var(--gold);
  }
</style>
</head>
<body>
<svg class="label-canvas" viewBox="0 0 1050 812" xmlns="http://www.w3.org/2000/svg">
  <rect class="label-ground" x="250.5" y="146.5" width="551" height="524"/>

  <path class="frame-outer" d="M372,236 H686 V250 H698 Q730,410 698,572 H686 V586 H372 V572 H360 Q326,410 360,250 H372 Z"/>
  <path class="frame-inner" d="M388,254 H668 V266 H679 Q708,410 679,554 H668 V567 H388 V554 H377 Q348,410 377,266 H388 Z"/>

  <path class="crest-shield" role="img" aria-label="Heraldic crest emblem on a gold shield"
        d="M465,173 H589 V262 Q589,322 527,322 Q465,322 465,262 Z"/>

  <text class="brand-name" x="525" y="440" text-anchor="middle" textLength="326" lengthAdjust="spacingAndGlyphs">MARROWIND</text>
  <text class="product-line" x="533" y="484" text-anchor="middle" textLength="333" lengthAdjust="spacingAndGlyphs">Ultra- Premium Vodka</text>

  <line class="divider-dots" x1="372" y1="495" x2="683" y2="495"/>

  <text class="origin-line" x="526" y="527" text-anchor="middle">BRISBANE</text>
  <text class="origin-line" x="526" y="551" text-anchor="middle">AUSTRALIA</text>
</svg>
</body>
</html>
```